New Business Card Design Project

We are looking for a talented individual to create a truly awesome/unique business card design for us. We are looking for a someone to design something that will really stand out from the crowd - we don't mind what ideas you come up with (ie embossed/flat/matte/shine etc etc) just wow us with your creativity.
Updates

Target Market(s)

Video Games Industry Professionals (all levels of seniority from QA Testers through to CEOs)

Contact Information for Business Card

Company logo (see upload)
Company name: Northbay Play Careers Ltd
Employee Name: Darren Elsby
Job title: CEO
Website: www.nbpc2go.example
Office +44 1632 960418
Mobile: +44 7700 900276
Email: darren@nbpc2go.example

Colors

Designer to choose colors to be used in the design.

Requirements
Must have
• The business card design MUST contain all the information listed in the BUSINESS CARD DETAILS box.
• You will see the colours that are relevant to us (ie company logo) in the uploaded imagery - however you do not have to use all these colours when designing the business card itself
• MUST BE DOUBLE SIDED

```html
<!DOCTYPE html>
<html lang="en">
<head>
<meta charset="utf-8">
<title>Northbay Play Careers – Business Card</title>
<link rel="stylesheet" href="https://fonts.googleapis.com/css2?family=Didact+Gothic&family=Open+Sans:wght@400;700&display=swap">
<style>
  :root {
    --navy: #1c2d5e;
    --orange: #f47b20;
    --ink: #2b2b2b;
    --paper: #ffffff;
    --backdrop: #e9e6e1;
  }
  * { margin: 0; padding: 0; box-sizing: border-box; }
  html, body { width: 1200px; height: 900px; overflow: hidden; }
  body { background: var(--backdrop); position: relative; font-family: "Open Sans", sans-serif; }

  .card { position: absolute; box-shadow: 2px 3px 6px rgba(0,0,0,.35); }

  .card-front { left: 329px; top: 90px; width: 556px; height: 345px; background: var(--paper); }
  .card-front .base-band { position: absolute; left: 0; bottom: 0; width: 100%; height: 16px; background: var(--navy); }

  .brand { position: absolute; left: 390px; top: 138px; display: flex; align-items: center; gap: 16px; }
  .brand-dot { width: 72px; height: 72px; border-radius: 50%; background: var(--navy); }
  .brand-name { font-family: "Open Sans", sans-serif; font-weight: 700; font-size: 28px; line-height: 32px; color: var(--navy); }

  .holder { position: absolute; left: 524px; top: 259px; }
  .holder-name { font-family: "Didact Gothic", sans-serif; font-size: 22px; line-height: 26px; color: var(--navy); letter-spacing: .3px; }
  .holder-role { font-size: 15px; line-height: 18px; color: var(--orange); }

  .contacts { position: absolute; left: 524px; top: 316px; list-style: none; }
  .contacts li { display: flex; align-items: center; gap: 6px; height: 20.3px; font-size: 16px; color: var(--ink); }
  .contacts svg { width: 12px; height: 12px; fill: var(--navy); flex: none; }

  .card-back { left: 329px; top: 469px; width: 560px; height: 344px; background: var(--navy); display: flex; align-items: center; justify-content: center; }
  .back-name { font-family: "Open Sans", sans-serif; font-weight: 700; font-size: 34px; color: var(--paper); }
</style>
</head>
<body>

<section class="card card-front">
  <div class="base-band"></div>
</section>

<div class="brand">
  <div class="brand-dot"></div>
  <div class="brand-name">Northbay Play<br>Careers</div>
</div>

<div class="holder">
  <div class="holder-name">Darren Elsby</div>
  <div class="holder-role">CEO</div>
</div>

<ul class="contacts">
  <li><svg viewBox="0 0 12 12"><path d="M1 4c0-2 2-3 5-3s5 1 5 3l-3 .5L7.5 3h-3L4 4.5zM2 6l2-1h4l2 1v4H2z"/></svg>+44 1632 960418</li>
  <li><svg viewBox="0 0 12 12"><path d="M3 0h6v12H3zM4 1.5v8h4v-8z"/></svg>+44 7700 900276</li>
  <li><svg viewBox="0 0 12 12"><path d="M1 2.5h10v7H1zM1.8 3.2 6 6.5l4.2-3.3"/></svg>darren@nbpc2go.example</li>
  <li><svg viewBox="0 0 12 12"><circle cx="6" cy="6" r="5.5"/></svg>www.nbpc2go.example</li>
</ul>

<section class="card card-back">
  <div class="back-name">Northbay Play Careers</div>
</section>

</body>
</html>
```